Painting Contractor Business Card Design

We are looking for a cool, bold, modern, polished, business card design. We are a high-end residential painting contractor. Please incorporate our logo and keep with our green/black color scheme. We are interested in seeing 2-sided and 1-sided options. Thank you very much!

Industry/Entity Type

Business

Contact Information for Business Card

Info for the card:
Owen Talsky
mobile 206-555-0193
email owen@kestrowfinish.net
web www.kestrowfinish.net

```html
<!DOCTYPE html>
<html lang="en">
<head>
<meta charset="utf-8">
<title>Kestrow Finish – Business Card</title>
<link href="https://fonts.googleapis.com/css2?family=Montserrat:wght@600&family=Open+Sans:wght@400;700;800&display=swap" rel="stylesheet">
<style>
  :root{
    --bg:#e9e7e3;
    --card-white:#ffffff;
    --card-black:#1e1e20;
    --panel-dark:#2f2f31;
    --brand-blue:#1268c8;
    --brand-green:#2bb24c;
    --ink:#1a1a1a;
    --ink-soft:#444444;
  }
  *{margin:0;padding:0;box-sizing:border-box}
  html,body{width:1200px;height:900px;overflow:hidden;background:var(--bg)}
  .stage{position:relative;width:1200px;height:900px}
  .card{position:absolute;left:250px;width:700px;height:400px;border-radius:28px;overflow:hidden;box-shadow:0 10px 30px rgba(0,0,0,.18)}
  .card svg.card-shapes{position:absolute;inset:0;width:100%;height:100%}

  /* Back side */
  .card-back{top:30px;background:var(--card-black);border:8px solid var(--brand-blue)}
  .back-wordmark{position:absolute;left:0;right:0;top:140px;text-align:center;
    font-family:"Montserrat",sans-serif;font-weight:600;font-size:54px;letter-spacing:6px;color:#ffffff}

  /* Front side */
  .card-front{top:470px;background:var(--card-white);border:8px solid var(--card-black)}
  .front-brand{position:absolute;left:44px;top:52px;display:flex;align-items:center;gap:18px}
  .brand-square{width:40px;height:40px;background:var(--brand-green)}
  .brand-name{font-family:"Montserrat",sans-serif;font-weight:600;font-size:44px;letter-spacing:3px;color:var(--ink)}
  .person{position:absolute;left:44px;top:200px}
  .person-name{font-family:"Open Sans",sans-serif;font-weight:800;font-size:32px;color:var(--ink);line-height:1}
  .person-role{font-family:"Open Sans",sans-serif;font-weight:400;font-size:17px;color:var(--brand-green);margin-top:6px}
  .contact{position:absolute;left:44px;top:292px;list-style:none;
    font-family:"Open Sans",sans-serif;font-size:19px;color:var(--ink-soft)}
  .contact li{display:flex;align-items:center;gap:12px;height:28px}
  .contact svg{width:16px;height:16px;flex:none}
</style>
</head>
<body>
<main class="stage">

  <section class="card card-back" aria-label="Card back">
    <svg class="card-shapes" viewBox="0 0 684 384" preserveAspectRatio="none" aria-hidden="true">
      <polygon points="0,225 0,384 440,384" fill="var(--brand-blue)"/>
    </svg>
    <p class="back-wordmark">KESTROW FINISH</p>
  </section>

  <section class="card card-front" aria-label="Card front">
    <svg class="card-shapes" viewBox="0 0 684 384" preserveAspectRatio="none" aria-hidden="true">
      <polygon points="684,70 684,384 520,384" fill="var(--panel-dark)"/>
      <line x1="40" y1="122" x2="650" y2="122" stroke="var(--ink)" stroke-width="1.5"/>
      <line x1="122" y1="240" x2="585" y2="240" stroke="var(--ink)" stroke-width="1.5"/>
    </svg>

    <div class="front-brand">
      <span class="brand-square"></span>
      <span class="brand-name">KESTROW FINISH</span>
    </div>

    <div class="person">
      <p class="person-name">Owen Talsky</p>
      <p class="person-role">Owner</p>
    </div>

    <ul class="contact">
      <li>
        <svg viewBox="0 0 16 16"><rect x="4" y="1" width="8" height="14" rx="1.5" fill="none" stroke="var(--brand-green)" stroke-width="1.6"/><circle cx="8" cy="12.3" r="0.9" fill="var(--brand-green)"/></svg>
        206-555-0193
      </li>
      <li>
        <svg viewBox="0 0 16 16"><rect x="1" y="3" width="14" height="10" rx="1" fill="none" stroke="var(--brand-green)" stroke-width="1.6"/><polyline points="1.5,3.5 8,9 14.5,3.5" fill="none" stroke="var(--brand-green)" stroke-width="1.6"/></svg>
        owen@kestrowfinish.net
      </li>
      <li>
        <svg viewBox="0 0 16 16"><circle cx="8" cy="8" r="6.5" fill="none" stroke="var(--brand-green)" stroke-width="1.5"/><ellipse cx="8" cy="8" rx="3" ry="6.5" fill="none" stroke="var(--brand-green)" stroke-width="1.2"/><line x1="1.5" y1="8" x2="14.5" y2="8" stroke="var(--brand-green)" stroke-width="1.2"/></svg>
        www.kestrowfinish.net
      </li>
    </ul>
  </section>

</main>
</body>
</html>
```